Sol Gorditas Digital Menu Boards

IF SELECTED, WINNER MAY BE HIRED FOR OTHER DESIGNS OF DIFFERENT STORES OF OUR COMPANY.

Task: Digital Menu Boards Design

Task description: We need designs for a Digital Menu to be displayed on two 42’’screens at Solgorditas, a fast-food restaurant in Guadalajara, Mexico. The menu redesign should communicate to our customers the experience of eating at our restaurant.

For avoiding the creation of videos, we are expecting several menu slides with the same text but with different images, simulating the effect of a video where the images are changing. This menu slides will be projected through a USB memory and a slideshow.

Attached files:
For the design, there are several documents attached to the task description:
1. Logo of the restaurant
2. Pictures of the restaurant
3. Example video of what we want to achieve through this menu slides.
4. Pictures of the actual menu board, to be replaced with the new designs.
5. Menu description (regular and breakfast menu)
6. Pictures of each element on the menu (We don’t have yet any breakfast pictures)
**The files are organized on a ZIP file.

Expected product:
For the regular menu,
• 2 menu slide designs for TACOS Y ESPECIALIDADES, where the text will be exactly the same but the images would differ.
• 2 menu slide designs for BEBIDAS Y EXTRAS, where the text will be exactly the same but the images would differ.
For the breakfast menu,
• 1 menu slide including all the menu
Total: 5 menu board slides.

Technical specs:
• You should send the editable file, med and high resolution JPGs for each design.
• The designs should fit perfectly on 42’’ screens.

```html
<!DOCTYPE html>
<html lang="es">
<head>
<meta charset="utf-8">
<title>Sol Gorditas — Bebidas</title>
<link rel="stylesheet" href="https://fonts.googleapis.com/css2?family=Arimo:wght@400;700&family=Kaushan+Script&display=swap">
<style>
  :root {
    --stripe-dark: #5e1f17;
    --stripe-light: #7d2c20;
    --parchment-light: #f0c98a;
    --parchment-dark: #c9803e;
    --brand-red: #c8102e;
    --cream: #fbd899;
    --panel-white: #ffffff;
    --ink: #1c1c1c;
    --photo-light: #e9eef2;
    --photo-warm: #b98a3a;
    --photo-green: #6f8a3a;
  }
  * { margin: 0; padding: 0; box-sizing: border-box; }
  html, body { width: 1200px; height: 669px; overflow: hidden; background: var(--stripe-dark); }
  .menu-board {
    position: relative;
    width: 1200px;
    height: 669px;
    overflow: hidden;
    background:
      linear-gradient(180deg, rgba(0,0,0,0.25), rgba(0,0,0,0) 30%, rgba(0,0,0,0) 70%, rgba(0,0,0,0.3)),
      repeating-linear-gradient(90deg, var(--stripe-light) 0 5px, var(--stripe-dark) 5px 9px);
    font-family: "Arimo", Arial, sans-serif;
  }
  .title-banner {
    position: absolute;
    left: 0; top: 92px;
    width: 920px; height: 162px;
    background: radial-gradient(ellipse at 45% 50%, var(--parchment-light), var(--parchment-dark) 85%);
    clip-path: polygon(0 6%, 12% 2%, 20% 8%, 34% 0, 48% 7%, 62% 1%, 76% 6%, 90% 0, 100% 5%, 98% 50%, 100% 96%, 86% 100%, 72% 93%, 58% 100%, 44% 94%, 30% 100%, 16% 94%, 0 98%);
  }
  .section-title {
    position: absolute;
    left: 295px; top: 118px;
    width: 300px;
    text-align: center;
    font-family: "Kaushan Script", cursive;
    font-size: 86px;
    line-height: 1;
    color: var(--brand-red);
    -webkit-text-stroke: 0;
    text-shadow: 0 0 0 #fff, 3px 0 #fff, -3px 0 #fff, 0 3px #fff, 0 -3px #fff, 3px 3px #fff, -3px -3px #fff, 3px -3px #fff, -3px 3px #fff, 5px 6px 6px rgba(0,0,0,0.45);
  }
  .brand {
    position: absolute;
    left: 830px; top: 10px;
    width: 345px; height: 300px;
  }
  .brand-circle {
    position: absolute;
    left: 96px; top: 0;
    width: 212px; height: 212px;
    border-radius: 50%;
    background: var(--cream);
    border: 8px solid #fff;
    box-shadow: 0 4px 10px rgba(0,0,0,0.35);
  }
  .brand-name {
    position: absolute;
    left: 0; top: 200px;
    width: 345px;
    text-align: center;
    font-family: "Kaushan Script", cursive;
    font-size: 56px;
    line-height: 1;
    color: #fff;
  }
  .menu-frame {
    position: absolute;
    left: 64px; top: 291px;
    width: 1076px; height: 316px;
    background: var(--cream);
    border-radius: 30px;
    box-shadow: 0 4px 12px rgba(0,0,0,0.35);
  }
  .price-list {
    position: absolute;
    left: 77px; top: 305px;
    width: 527px; height: 289px;
    background: var(--panel-white);
    border-radius: 34px;
    text-align: center;
    color: var(--ink);
    padding-top: 12px;
  }
  .item-name { font-size: 34px; line-height: 34px; font-weight: 400; letter-spacing: -0.5px; transform: scaleX(0.92); }
  .item-price { font-size: 50px; line-height: 46px; font-weight: 700; color: var(--brand-red); transform: scaleX(0.88); margin-bottom: 2px; }
  .drinks-photo {
    position: absolute;
    left: 627px; top: 305px;
    width: 500px; height: 289px;
    border-radius: 0 30px 30px 0;
    background:
      linear-gradient(180deg, rgba(0,0,0,0) 45%, rgba(255,255,255,0.7) 60%, rgba(255,255,255,0.7) 100%),
      linear-gradient(90deg, var(--photo-warm) 0 22%, var(--photo-light) 22% 44%, var(--photo-warm) 44% 62%, var(--photo-light) 62% 78%, var(--photo-green) 78% 94%, var(--photo-light) 94%);
  }
</style>
</head>
<body>
<main class="menu-board">
  <div class="title-banner" role="img" aria-label="Torn parchment banner"></div>
  <h1 class="section-title">Bebidas</h1>

  <div class="brand">
    <div class="brand-circle"></div>
    <div class="brand-name">Sol Gorditas</div>
  </div>

  <div class="menu-frame"></div>
  <section class="price-list">
    <p class="item-name">CERVEZA NACIONAL</p>
    <p class="item-price">30</p>
    <p class="item-name">CERVEZA IMPORTADA</p>
    <p class="item-price">40</p>
    <p class="item-name">AGUA EMBOTELLADA/REFRESCO</p>
    <p class="item-price">16</p>
  </section>
  <div class="drinks-photo" role="img" aria-label="Photo of three beer bottles behind a plate with guacamole, tortilla chips, pico de gallo and lime wedges"></div>
</main>
</body>
</html>
```